Criação de Projeto Combo top of mind para Tecnologia & Ciencias
A empresa queria:
" A empresa é formada por um casal, uma advogada e especialista em tecnologia. Oferecemos um serviço especializado para área jurídica que tem dificuldades especificas, e não pode parar nenhum minuto por causa dos prazos. A ideia da empresa surgiu pois como advogada e consumidora não encontrei nenhum TI especializado na área. Ofereceremos suporte técnico, consultoria, transferência de servidores para a nuvem, etc. "

```html
<!DOCTYPE html>
<html lang="pt-BR">
<head>
<meta charset="UTF-8">
<title>NOVIX — Papel de parede</title>
<link href="https://fonts.googleapis.com/css2?family=Montserrat:wght@500;600&display=swap" rel="stylesheet">
<style>
  :root {
    --page-bg: #eceeef;
    --blue-deep: #3f63ee;
    --blue-mid: #2f8df3;
    --cyan-light: #18d2f7;
    --white: #ffffff;
    --wave-glow: rgba(255, 255, 255, 0.28);
  }
  * { margin: 0; padding: 0; box-sizing: border-box; }
  html, body {
    width: 1200px;
    height: 1200px;
    overflow: hidden;
    background: var(--page-bg);
  }
  .canvas {
    position: relative;
    width: 1200px;
    height: 1200px;
    display: flex;
    align-items: center;
    justify-content: center;
  }
  .wallpaper {
    position: relative;
    width: 1200px;
    height: 675px;
    overflow: hidden;
    background: linear-gradient(30deg, var(--blue-deep) 0%, var(--blue-mid) 50%, var(--cyan-light) 100%);
  }
  .wave-decoration {
    position: absolute;
    left: 0;
    top: 0;
    width: 320px;
    height: 675px;
    background:
      radial-gradient(ellipse 160px 340px at 90px 300px, var(--wave-glow), transparent 70%),
      linear-gradient(90deg, rgba(255,255,255,0.14), rgba(255,255,255,0));
  }
  .brand {
    position: absolute;
    right: 52px;
    bottom: 30px;
    width: 200px;
    display: flex;
    flex-direction: column;
    align-items: center;
    color: var(--white);
    font-family: "Montserrat", sans-serif;
  }
  .brand-dot {
    width: 92px;
    height: 92px;
    border-radius: 50%;
    border: 2px solid var(--white);
    margin-bottom: 14px;
  }
  .brand-name {
    font-weight: 600;
    font-size: 56px;
    line-height: 1;
    letter-spacing: 2px;
  }
  .brand-tagline {
    margin-top: 8px;
    font-weight: 500;
    font-size: 11.5px;
    letter-spacing: 3.2px;
    white-space: nowrap;
  }
</style>
</head>
<body>
  <main class="canvas">
    <section class="wallpaper">
      <div class="wave-decoration" role="img" aria-label="Linhas onduladas finas e translúcidas em branco fluindo verticalmente"></div>
      <div class="brand">
        <div class="brand-dot"></div>
        <div class="brand-name">NOVIX</div>
        <div class="brand-tagline">SOLUÇÕES TECNOLÓGICAS</div>
      </div>
    </section>
  </main>
</body>
</html>
```